TideForge, LLC
Business Cards - Consulting
Business Cards
Professional
Desmond K Harlow
President
318 Quillfeather Court Brownsburg, IN 46219
dharlow4872@mailnest.example

```html
<!DOCTYPE html>
<html lang="en">
<head>
<meta charset="utf-8">
<title>TideForge, LLC – Stationery</title>
<link href="https://fonts.googleapis.com/css2?family=Roboto:wght@400;700&display=swap" rel="stylesheet">
<style>
  :root {
    --bg: #8d8e90;
    --paper: #ffffff;
    --green: #3cae49;
    --navy: #2d4466;
    --ink: #4a4f57;
    --faint: #e6ece8;
  }
  * { margin: 0; padding: 0; box-sizing: border-box; }
  html, body { width: 1200px; height: 626px; overflow: hidden; }
  body { background: var(--bg); font-family: "Roboto", Arial, sans-serif; position: relative; color: var(--ink); }

  .sheet { position: absolute; background: var(--paper); overflow: hidden; box-shadow: 0 2px 6px rgba(0,0,0,.25); }

  .brand { position: absolute; display: flex; align-items: center; gap: 5px; }
  .brand-dot { border-radius: 50%; background: var(--green); flex: none; }
  .brand-text { display: flex; flex-direction: column; line-height: 1; }
  .brand-name { font-weight: 700; color: var(--navy); letter-spacing: .3px; }
  .brand-tag { color: var(--green); font-weight: 400; margin-top: 2px; white-space: nowrap; }

  .bars { position: absolute; left: 0; right: 0; bottom: 0; display: flex; }
  .bar-green { background: var(--green); }
  .bar-navy { background: var(--navy); flex: 1; }

  .fine { position: absolute; font-size: 4px; color: var(--ink); white-space: nowrap; }

  .watermark { position: absolute; border-radius: 50%; border: solid var(--faint); }

  /* business card front */
  .card-front { left: 34px; top: 197px; width: 182px; height: 96px; }
  .card-front .brand { left: 34px; top: 34px; }
  .card-front .brand-dot { width: 22px; height: 22px; }
  .card-front .brand-name { font-size: 15px; }
  .card-front .brand-tag { font-size: 4.5px; }

  /* business card back */
  .card-back { left: 34px; top: 307px; width: 182px; height: 96px; }
  .card-back .brand { left: 8px; top: 9px; }
  .card-back .brand-dot { width: 16px; height: 16px; }
  .card-back .brand-name { font-size: 11px; }
  .card-back .brand-tag { font-size: 3.5px; }
  .person { position: absolute; left: 10px; top: 40px; }
  .person-name { font-size: 6px; font-weight: 700; color: var(--navy); }
  .person-title { font-size: 4.5px; color: var(--ink); margin-top: 1px; }
  .card-back .fine { left: 10px; bottom: 9px; }
  .card-back .bar-green { width: 50px; height: 4px; }
  .card-back .bar-navy { height: 4px; }

  /* letterhead */
  .letterhead { left: 233px; top: 29px; width: 432px; height: 561px; }
  .letterhead .brand { left: 22px; top: 18px; }
  .letterhead .brand-dot { width: 24px; height: 24px; }
  .letterhead .brand-name { font-size: 16px; }
  .letterhead .brand-tag { font-size: 5px; }
  .letterhead .watermark { width: 200px; height: 200px; border-width: 16px; right: 20px; bottom: 40px; }
  .letterhead .fine { left: 20px; bottom: 14px; }
  .letterhead .bar-green { width: 76px; height: 6px; }
  .letterhead .bar-navy { height: 6px; margin-left: 4px; }

  /* envelope back */
  .envelope-back { left: 679px; top: 91px; width: 490px; height: 245px; }
  .flap { position: absolute; inset: 0; }
  .envelope-back .brand { left: 50%; top: 98px; transform: translateX(-50%); flex-direction: column; }
  .envelope-back .brand-dot { width: 24px; height: 24px; }
  .envelope-back .brand-name { font-size: 9px; }

  /* envelope front */
  .envelope-front { left: 679px; top: 343px; width: 490px; height: 250px; }
  .envelope-front .brand { left: 20px; top: 62px; }
  .envelope-front .brand-dot { width: 22px; height: 22px; }
  .envelope-front .brand-name { font-size: 15px; }
  .envelope-front .brand-tag { font-size: 4.5px; }
  .envelope-front .watermark { width: 150px; height: 150px; border-width: 12px; right: 28px; top: 40px; }
  .envelope-front .fine { left: 20px; bottom: 22px; }
  .envelope-front .bar-green { width: 86px; height: 9px; }
  .envelope-front .bar-navy { height: 9px; margin-left: 4px; }
</style>
</head>
<body>

<section class="sheet card-front" aria-label="Business card front">
  <div class="brand">
    <span class="brand-dot"></span>
    <div class="brand-text">
      <span class="brand-name">TideForge</span>
      <span class="brand-tag">Consulting and Professional Services</span>
    </div>
  </div>
</section>

<section class="sheet card-back" aria-label="Business card back">
  <div class="brand">
    <span class="brand-dot"></span>
    <div class="brand-text">
      <span class="brand-name">TideForge</span>
      <span class="brand-tag">Consulting and Professional Services</span>
    </div>
  </div>
  <div class="person">
    <div class="person-name">Desmond K Harlow</div>
    <div class="person-title">President</div>
  </div>
  <p class="fine">p 317-555-0148 | dharlow4872@mailnest.example | 318 Quillfeather Court Brownsburg, IN 46219</p>
  <div class="bars"><span class="bar-green"></span><span class="bar-navy"></span></div>
</section>

<section class="sheet letterhead" aria-label="Letterhead">
  <div class="brand">
    <span class="brand-dot"></span>
    <div class="brand-text">
      <span class="brand-name">TideForge</span>
      <span class="brand-tag">Consulting and Professional Services</span>
    </div>
  </div>
  <div class="watermark"></div>
  <p class="fine">p 317-555-0148 | e dharlow4872@mailnest.example | 318 Quillfeather Court Brownsburg, IN 46219</p>
  <div class="bars"><span class="bar-green"></span><span class="bar-navy"></span></div>
</section>

<section class="sheet envelope-back" aria-label="Envelope back">
  <svg class="flap" viewBox="0 0 490 245" preserveAspectRatio="none" aria-hidden="true">
    <polyline points="0,70 245,140 490,70" fill="none" stroke="#d5d7da" stroke-width="1"/>
    <line x1="0" y1="70" x2="490" y2="70" stroke="#eceef0" stroke-width="1"/>
  </svg>
  <div class="brand">
    <span class="brand-dot"></span>
    <span class="brand-name">TideForge</span>
  </div>
</section>

<section class="sheet envelope-front" aria-label="Envelope front">
  <div class="brand">
    <span class="brand-dot"></span>
    <div class="brand-text">
      <span class="brand-name">TideForge</span>
      <span class="brand-tag">Consulting and Professional Services</span>
    </div>
  </div>
  <div class="watermark"></div>
  <p class="fine">p 317-555-0148 | e dharlow4872@mailnest.example | 318 Quillfeather Court Brownsburg, IN 46219</p>
  <div class="bars"><span class="bar-green"></span><span class="bar-navy"></span></div>
</section>

</body>
</html>
```